"Mirren Hatch" Mobile 2D Game

We need a mobile design for the main screen of the game (with a popup design to select the ball color), for a Professional IT Team. Our initial game is "Mirren Hatch", classic board game for kids and even non kids. We would like to see design that suitable for mobile devices (small and tablet). The main concept of the game will be something similar to this video link: https://www.vidstorn.com/watch?v=QtR8kLmzPwe

Please be sure the balls inside the game board have readable numbers. Thanks!

Requirements
Must have
• Separate layers for each UI component so it can be exported easily

```html
<!DOCTYPE html>
<html lang="en">
<head>
<meta charset="utf-8">
<title>Game Screens – Ball Select and Board</title>
<link rel="stylesheet" href="https://fonts.googleapis.com/css2?family=Bebas+Neue&display=swap">
<style>
  :root {
    --page-bg: #ffffff;
    --screen-bg: #f2f2f2;
    --screen-edge: #d9d9d9;
    --brown: #6b4a12;
    --brown-dark: #5c4516;
    --shadow: #bdbdbd;
    --gold-top: #f7d04a;
    --gold-bottom: #f0a91c;
    --green-top: #33ee66;
    --green-bottom: #6ccb23;
    --orange-top: #f3c31c;
    --orange-bottom: #ff5146;
    --cell-line: #6b4a12;
    --white: #ffffff;
  }
  * { margin: 0; padding: 0; box-sizing: border-box; }
  html, body { width: 867px; height: 1200px; overflow: hidden; }
  body { background: var(--page-bg); position: relative; font-family: "Bebas Neue", sans-serif; }
  .screen {
    position: absolute;
    left: 117px;
    width: 632px;
    height: 291px;
    border-radius: 30px;
    background: var(--screen-bg);
    box-shadow: 0 0 0 1px var(--screen-edge);
    overflow: hidden;
  }
  .screen--ball-select { top: 230px; }
  .screen--board { top: 648px; }
  .screen svg { display: block; width: 100%; height: 100%; }
  .label { font-family: "Bebas Neue", sans-serif; fill: var(--brown); text-anchor: middle; }
  .label--light { fill: var(--white); stroke: var(--brown); stroke-width: 0.6; paint-order: stroke; }
  .btn-shadow, .ball-shadow { fill: var(--shadow); }
  .outline { stroke: var(--brown); stroke-width: 1.3; }
  .grid-line { stroke: var(--cell-line); stroke-width: 1.2; fill: none; }
  .block { fill: var(--brown-dark); }
  .arrow { fill: var(--brown); }
  .hole { fill: var(--brown-dark); stroke: var(--gold-bottom); stroke-width: 1.5; }
</style>
</head>
<body>

<section class="screen screen--ball-select" aria-label="Ball colour selection">
  <svg viewBox="0 0 632 291" xmlns="http://www.w3.org/2000/svg">
    <defs>
      <linearGradient id="gold" x1="0" y1="0" x2="0" y2="1">
        <stop offset="0" style="stop-color:var(--gold-top)"/>
        <stop offset="1" style="stop-color:var(--gold-bottom)"/>
      </linearGradient>
      <linearGradient id="green" x1="0" y1="0" x2="0" y2="1">
        <stop offset="0" style="stop-color:var(--green-top)"/>
        <stop offset="1" style="stop-color:var(--green-bottom)"/>
      </linearGradient>
      <linearGradient id="orange" x1="0" y1="0" x2="0" y2="1">
        <stop offset="0" style="stop-color:var(--orange-top)"/>
        <stop offset="1" style="stop-color:var(--orange-bottom)"/>
      </linearGradient>
    </defs>

    <text class="label title" x="308" y="97" font-size="31" letter-spacing="0.6">CHOOSE THE COLOR OF YOUR BALL:</text>

    <g class="ball-choice ball-choice--green">
      <circle class="ball-shadow" cx="229" cy="175" r="41"/>
      <circle class="outline" cx="229" cy="168" r="41" fill="url(#green)"/>
    </g>
    <g class="ball-choice ball-choice--orange">
      <circle class="ball-shadow" cx="391" cy="175" r="41"/>
      <circle class="outline" cx="391" cy="168" r="41" fill="url(#orange)"/>
    </g>

    <g class="button button--tutorial">
      <rect class="btn-shadow" x="15" y="248" width="85" height="36" rx="18"/>
      <rect class="outline" x="15" y="244" width="85" height="36" rx="18" fill="url(#gold)"/>
      <text class="label" x="57.5" y="271" font-size="21">TUTORIAL</text>
    </g>
    <g class="button button--options">
      <rect class="btn-shadow" x="531" y="250" width="86" height="36" rx="18"/>
      <rect class="outline" x="531" y="246" width="86" height="36" rx="18" fill="url(#gold)"/>
      <text class="label" x="574" y="274" font-size="24">OPTIONS</text>
    </g>
  </svg>
</section>

<section class="screen screen--board" aria-label="Game board">
  <svg viewBox="0 0 632 291" xmlns="http://www.w3.org/2000/svg">
    <defs>
      <linearGradient id="gold2" x1="0" y1="0" x2="0" y2="1">
        <stop offset="0" style="stop-color:var(--gold-top)"/>
        <stop offset="1" style="stop-color:var(--gold-bottom)"/>
      </linearGradient>
      <linearGradient id="green2" x1="0" y1="0" x2="0" y2="1">
        <stop offset="0" style="stop-color:var(--green-top)"/>
        <stop offset="1" style="stop-color:var(--green-bottom)"/>
      </linearGradient>
      <linearGradient id="orange2" x1="0" y1="0" x2="0" y2="1">
        <stop offset="0" style="stop-color:var(--orange-top)"/>
        <stop offset="1" style="stop-color:var(--orange-bottom)"/>
      </linearGradient>
      <symbol id="arrow-right" viewBox="0 0 20 20">
        <path class="arrow" d="M3 7h8V3l7 7-7 7v-4H3z"/>
      </symbol>
    </defs>

    <!-- header buttons -->
    <g class="button button--help">
      <rect class="btn-shadow" x="17" y="13" width="39" height="23" rx="11.5"/>
      <rect class="outline" x="17" y="10" width="39" height="23" rx="11.5" fill="url(#gold2)"/>
      <text class="label" x="36.5" y="29" font-size="19">?</text>
    </g>
    <g class="button button--score">
      <rect class="btn-shadow" x="578" y="13" width="39" height="23" rx="11.5"/>
      <rect class="outline" x="578" y="10" width="39" height="23" rx="11.5" fill="url(#gold2)"/>
      <text class="label" x="597.5" y="27" font-size="13">SCORE</text>
    </g>

    <!-- player scores -->
    <g class="score score--green">
      <circle class="ball-shadow" cx="108" cy="146" r="24"/>
      <circle class="outline" cx="108" cy="142" r="24" fill="url(#green2)"/>
      <text class="label label--light" x="108" y="151" font-size="25">600</text>
    </g>
    <g class="score score--orange">
      <circle class="ball-shadow" cx="539" cy="146" r="24"/>
      <circle class="outline" cx="539" cy="142" r="24" fill="url(#orange2)"/>
      <text class="label label--light" x="539" y="151" font-size="25">130</text>
    </g>

    <!-- board -->
    <g class="board" transform="translate(180 36)">
      <g class="board-cells">
        <rect class="block" x="162.6" y="27.1" width="27.1" height="27.1"/>
        <rect class="block" x="27.1" y="81.3" width="27.1" height="27.1"/>
        <rect class="block" x="162.6" y="162.6" width="27.1" height="27.1"/>
        <rect fill="url(#gold2)" x="81.3" y="54.2" width="27.1" height="27.1"/>
        <rect fill="url(#gold2)" x="162.6" y="81.3" width="27.1" height="27.1"/>
        <rect fill="url(#gold2)" x="27.1" y="162.6" width="27.1" height="27.1"/>
        <use href="#arrow-right" x="85.3" y="57.7" width="19" height="19"/>
        <use href="#arrow-right" x="166.6" y="84.8" width="19" height="19" transform="rotate(180 176.15 94.85)"/>
        <use href="#arrow-right" x="31.1" y="166.1" width="19" height="19" transform="rotate(180 40.65 176.15)"/>
      </g>

      <g class="grid">
        <rect class="grid-line" x="0" y="0" width="271" height="216.8"/>
        <path class="grid-line" d="M27.1 0v216.8M54.2 0v216.8M81.3 0v216.8M108.4 0v216.8M135.5 0v216.8M162.6 0v216.8M189.7 0v216.8M216.8 0v216.8M243.9 0v216.8
                                   M0 27.1h271M0 54.2h271M0 81.3h271M0 108.4h271M0 135.5h271M0 162.6h271M0 189.7h271"/>
      </g>

      <g class="start-balls">
        <circle class="outline" cx="13.55" cy="13.55" r="9.5" fill="url(#orange2)"/>
        <circle class="outline" cx="40.65" cy="13.55" r="9.5" fill="url(#orange2)"/>
        <circle class="outline" cx="67.75" cy="13.55" r="9.5" fill="url(#orange2)"/>
        <circle class="outline" cx="94.85" cy="13.55" r="9.5" fill="url(#orange2)"/>
        <circle class="outline" cx="121.95" cy="13.55" r="9.5" fill="url(#orange2)"/>
        <circle class="outline" cx="149.05" cy="13.55" r="9.5" fill="url(#orange2)"/>
        <circle class="outline" cx="176.15" cy="13.55" r="9.5" fill="url(#orange2)"/>
        <circle class="outline" cx="203.25" cy="13.55" r="9.5" fill="url(#orange2)"/>
        <circle class="outline" cx="230.35" cy="13.55" r="9.5" fill="url(#orange2)"/>
        <circle class="outline" cx="257.45" cy="13.55" r="9.5" fill="url(#orange2)"/>
      </g>

      <g class="point-balls">
        <circle class="outline" cx="67.75" cy="67.75" r="9.5" fill="url(#green2)"/>
        <text class="label label--light" x="67.75" y="73" font-size="13">10</text>
        <circle class="outline" cx="257.45" cy="67.75" r="9.5" fill="url(#orange2)"/>
        <text class="label label--light" x="257.45" y="73" font-size="13">20</text>
        <circle class="outline" cx="203.25" cy="94.85" r="9.5" fill="url(#green2)"/>
        <text class="label label--light" x="203.25" y="100" font-size="13">10</text>
        <circle class="outline" cx="121.95" cy="121.95" r="9.5" fill="url(#orange2)"/>
        <text class="label label--light" x="121.95" y="127" font-size="13">20</text>
      </g>

      <g class="cell-values">
        <text class="label" x="13" y="130" font-size="19">10</text>
        <text class="label" x="203.25" y="157" font-size="19">20</text>
      </g>

      <g class="exit-holes" transform="translate(0 230)">
        <ellipse class="hole" cx="13.55" cy="0" rx="11.5" ry="4"/>
        <ellipse class="hole" cx="40.65" cy="0" rx="11.5" ry="4"/>
        <ellipse class="hole" cx="67.75" cy="0" rx="11.5" ry="4"/>
        <ellipse class="hole" cx="94.85" cy="0" rx="11.5" ry="4"/>
        <ellipse class="hole" cx="121.95" cy="0" rx="11.5" ry="4"/>
        <ellipse class="hole" cx="149.05" cy="0" rx="11.5" ry="4"/>
        <ellipse class="hole" cx="176.15" cy="0" rx="11.5" ry="4"/>
        <ellipse class="hole" cx="203.25" cy="0" rx="11.5" ry="4"/>
        <ellipse class="hole" cx="230.35" cy="0" rx="11.5" ry="4"/>
        <ellipse class="hole" cx="257.45" cy="0" rx="11.5" ry="4"/>
        <path class="outline" d="M248 0a9.5 9.5 0 0 1 19 0z" fill="url(#orange2)"/>
      </g>
    </g>

    <!-- footer buttons -->
    <g class="button button--back">
      <rect class="btn-shadow" x="13" y="249" width="85" height="36" rx="18"/>
      <rect class="outline" x="13" y="245" width="85" height="36" rx="18" fill="url(#gold2)"/>
      <text class="label" x="55.5" y="274" font-size="26">BACK</text>
    </g>
    <g class="button button--options">
      <rect class="btn-shadow" x="534" y="249" width="86" height="36" rx="18"/>
      <rect class="outline" x="534" y="245" width="86" height="36" rx="18" fill="url(#gold2)"/>
      <text class="label" x="577" y="273" font-size="24">OPTIONS</text>
    </g>
  </svg>
</section>

</body>
</html>
```